Trevolar bonds (Surety bond broker)

We are a broker of surety bonds, we need a presentation and a flyer with fresh design. Our core values are reliable, on time and customized service. We want to transmit to our clients, they can leave on us the process of underwriting and issuing a surety bond, so they can focus on their business with no distractions.

Font styles to use
Sans Serif
Other font styles liked:
• view logos

Requirements
Must have
• Visually attractive.
Main Message: Fast service issuing and underwriting surety bonds, reliable, nos surprises, we are always one step ahead, customized and personalized bonding solutions.
Nice to have
• Have short version for the flyer, and extended version for the presentation.
Should not have
• We already have a logo (attached), maintain colors

```html
<!DOCTYPE html>
<html lang="es">
<head>
<meta charset="utf-8">
<title>Trevolar bonds · Índice</title>
<link rel="stylesheet" href="https://fonts.googleapis.com/css2?family=Zilla+Slab:wght@700&family=Bitter:wght@400;500&display=swap">
<style>
  :root {
    --green: #67a83f;
    --green-dark: #4f9a34;
    --ink: #1f1f1f;
    --swoosh-black: #222222;
    --paper: #ffffff;
    --wash-1: #a9d98a;
    --wash-2: #d7ee9c;
    --sand: #a6804a;
    --sky: #b9c9c4;
  }
  html, body {
    margin: 0;
    padding: 0;
    width: 1200px;
    height: 848px;
    overflow: hidden;
    background: var(--paper);
  }
  .index-page {
    position: relative;
    width: 1200px;
    height: 848px;
    overflow: hidden;
  }
  .backdrop {
    position: absolute;
    inset: 0;
  }
  .index-title {
    position: absolute;
    left: 684px;
    top: 78px;
    margin: 0;
    font-family: "Zilla Slab", serif;
    font-weight: 700;
    font-size: 82px;
    line-height: 1;
    color: var(--green);
  }
  .chapter-list {
    position: absolute;
    left: 686px;
    top: 226px;
    margin: 0;
    padding: 0;
    list-style: none;
    font-family: "Bitter", serif;
    font-size: 24px;
    color: var(--ink);
  }
  .chapter-list li {
    height: 76.6px;
    display: flex;
    align-items: flex-start;
  }
  .chapter-number {
    color: var(--green);
    width: 22px;
  }
  .chapter-bar {
    color: var(--green);
    margin-right: 12px;
  }
  .brand {
    position: absolute;
    left: 964px;
    top: 768px;
    display: flex;
    align-items: center;
    gap: 10px;
  }
  .brand-dot {
    width: 16px;
    height: 16px;
    border-radius: 50%;
    background: var(--green);
  }
  .brand-name {
    font-family: "Bitter", serif;
    font-weight: 400;
    font-size: 38px;
    letter-spacing: 1px;
    color: var(--green);
  }
</style>
</head>
<body>
<main class="index-page">
  <svg class="backdrop" width="1200" height="848" viewBox="0 0 1200 848" xmlns="http://www.w3.org/2000/svg">
    <defs>
      <linearGradient id="page-wash" x1="1" y1="0" x2="0.2" y2="1">
        <stop offset="0" stop-color="var(--wash-1)"/>
        <stop offset="0.45" stop-color="var(--wash-2)" stop-opacity="0.75"/>
        <stop offset="1" stop-color="#ffffff"/>
      </linearGradient>
      <linearGradient id="pier-tones" x1="0" y1="0" x2="0" y2="1">
        <stop offset="0" stop-color="#b07a2a"/>
        <stop offset="0.38" stop-color="#7c5a2c"/>
        <stop offset="0.5" stop-color="var(--sky)"/>
        <stop offset="0.56" stop-color="#8f7a52"/>
        <stop offset="1" stop-color="var(--sand)"/>
      </linearGradient>
    </defs>
    <rect width="1200" height="848" fill="url(#page-wash)"/>
    <path role="img" aria-label="Photograph of a beach pier seen from below at sunset"
          d="M0 0 H528 C 470 300, 330 600, 150 848 H0 Z" fill="url(#pier-tones)"/>
    <path class="swoosh-black" d="M548 0 H650 C 600 300, 430 610, 178 830 C 390 600, 505 320, 548 0 Z" fill="var(--swoosh-black)"/>
    <path class="swoosh-green" d="M636 88 C 600 360, 440 640, 186 848 H226 C 460 630, 610 380, 636 88 Z" fill="var(--green-dark)"/>
    <path class="swoosh-green-thin" d="M432 612 C 380 720, 320 790, 258 848 H292 C 350 790, 400 720, 432 612 Z" fill="var(--green-dark)"/>
  </svg>

  <h1 class="index-title">Índice</h1>

  <ol class="chapter-list">
    <li><span class="chapter-number">1</span><span class="chapter-bar">|</span>¿Quiénes somos?</li>
    <li><span class="chapter-number">2</span><span class="chapter-bar">|</span>Oferta de Valor</li>
    <li><span class="chapter-number">3</span><span class="chapter-bar">|</span>Nuestros Servicios</li>
    <li><span class="chapter-number">4</span><span class="chapter-bar">|</span>Productos</li>
    <li><span class="chapter-number">5</span><span class="chapter-bar">|</span>Ciclo de administración de Fianzas</li>
    <li><span class="chapter-number">6</span><span class="chapter-bar">|</span>Nuestros socios de negocio</li>
    <li><span class="chapter-number">7</span><span class="chapter-bar">|</span>Contacto</li>
  </ol>

  <div class="brand">
    <span class="brand-dot"></span>
    <span class="brand-name">TREVOLAR</span>
  </div>
</main>
</body>
</html>
```